Desserts Business Card Design

I own a dessert business and cakes and cupcakes are my biggest sellers. I have been running this as a part time business since 2007. I am now looking to expand going full time and open a store front within he next 12 months.
With this expansion I am looking to have my own design setup for the business.

I have been using a design on my cards provided to me by a website I got the cards from. I would like a more original design I can use for the cards, the store front and any other advertising I will be doing. I also have a saying on the back of my business card which I would like to be worked in as well.
"Sweets are never better than homemade"

Target Market(s)

Younger and older families of all ethnic backgrounds

Industry/Entity Type

Advertising

Contact Information for Business Card

Maribel's Sugared Treats
Tobias Fenwick
4417 Pinecrest Terrace
Oshawa, Ontario
M3P 7J2

Logo Text

Logo styles of interest
Emblem Logo
Pictorial/Combination Logo
Wordmark Logo
Lettermark Logo
Requirements
Must have
• "Sweets are never better than homemade"
Nice to have
• Maribel's Sugared Treats - This can actually be turned into a logo which is really what I am looking for. Using MST, converted to a logo? I am really looking to see what you can provide me with.
A cake or cupcake added on the front of the card?
Should not have
• I cannot think of anything right now. I an looking forward to see the imaginations from the design groups

```html
<!DOCTYPE html>
<html lang="en">
<head>
<meta charset="utf-8">
<title>Maribel's Sugared Treats – Business Card</title>
<link href="https://fonts.googleapis.com/css2?family=Playfair+Display:ital,wght@1,600&family=Montserrat:wght@400;600&display=swap" rel="stylesheet">
<style>
  :root {
    --chocolate: #3d2314;
    --blush: #f5a5ab;
    --cream-pink: #fbc9b8;
    --rose: #e8898f;
    --frosting: #ffffff;
    --canvas: #ffffff;
    --card-shadow: rgba(40, 20, 10, 0.45);
  }
  * { margin: 0; padding: 0; box-sizing: border-box; }
  html, body { width: 1200px; height: 1000px; overflow: hidden; background: var(--canvas); }
  .stage { position: relative; width: 1200px; height: 1000px; }

  .card {
    position: absolute;
    top: 292px;
    width: 524px;
    height: 313px;
    border-radius: 22px;
    overflow: hidden;
    box-shadow: 6px 10px 12px var(--card-shadow);
  }
  .card--front { left: 46px; background: var(--chocolate); }
  .card--back { left: 628px; background: var(--blush); }

  .brand-name {
    position: absolute;
    left: 22px;
    top: 236px;
    font-family: "Playfair Display", serif;
    font-style: italic;
    font-weight: 600;
    font-size: 21px;
    line-height: 29px;
    color: var(--cream-pink);
  }
  .brand-seal {
    position: absolute;
    left: 382px;
    top: 176px;
    width: 130px;
    height: 130px;
    border-radius: 50%;
    background: radial-gradient(circle at 45% 45%, #f7b7bb, var(--rose));
  }

  .tagline {
    position: absolute;
    left: 0;
    top: 8px;
    width: 100%;
    padding-right: 20px;
    text-align: center;
    font-family: "Playfair Display", serif;
    font-style: italic;
    font-weight: 600;
    font-size: 33px;
    line-height: 46px;
    color: var(--chocolate);
  }
  .contact-rule {
    position: absolute;
    left: 14px;
    top: 112px;
    width: 14px;
    height: 186px;
  }
  .contact {
    position: absolute;
    left: 49px;
    top: 124px;
    width: 370px;
    font-family: "Montserrat", sans-serif;
    color: var(--chocolate);
  }
  .contact__name { font-weight: 600; font-size: 21px; line-height: 26px; margin-bottom: 11px; }
  .contact__line { font-size: 16px; line-height: 20px; margin-bottom: 7px; }
  .cupcake-art {
    position: absolute;
    left: 426px;
    top: 76px;
    width: 110px;
    height: 172px;
    border-radius: 50% 0 0 30%;
    background: linear-gradient(180deg, var(--frosting) 0%, var(--frosting) 48%, var(--cream-pink) 52%, #f3b6a6 100%);
  }
</style>
</head>
<body>
<main class="stage">
  <section class="card card--front" aria-label="Card front">
    <div class="brand-seal" role="img" aria-label="Round peeling sticker with a cupcake illustration"></div>
    <p class="brand-name">Maribel's<br>Sugared Treats</p>
  </section>

  <section class="card card--back" aria-label="Card back">
    <p class="tagline">‘Sweets are never better,<br>than homemade’</p>
    <svg class="contact-rule" viewBox="0 0 14 186" aria-hidden="true">
      <circle cx="7" cy="7" r="5" fill="none" stroke="#3d2314" stroke-width="1.6"/>
      <line x1="7" y1="14" x2="7" y2="172" stroke="#3d2314" stroke-width="2" stroke-dasharray="3 4"/>
      <circle cx="7" cy="179" r="5" fill="none" stroke="#3d2314" stroke-width="1.6"/>
    </svg>
    <div class="contact">
      <p class="contact__name">Tobias Fenwick</p>
      <p class="contact__line">289 555 0147</p>
      <p class="contact__line">4417 Pinecrest Terrace, Larkfield, Ontario<br>M3P7J2</p>
      <p class="contact__line">www.maribelstreats.com</p>
      <p class="contact__line">hello.sweetness@maribelstreats.com</p>
    </div>
    <div class="cupcake-art" role="img" aria-label="Cupcake illustration with white frosting and a cherry, cropped at the card edge"></div>
  </section>
</main>
</body>
</html>
```